author needs cover design for self publishing

Title. Lost in the rain, lost in the snow
Author. Trevor Hanley. I am a first time unknown author, so I doubt my name will sell!
Genre. A love story - the couple are married and in their early 30s
Time line. 30th January 1942, two weeks before Singapore surrenders.
Setting. Singapore docks- bombed and on fire, The SS Countess of Ashvale (the ships name on the cover is not important) is evacuating 1000 women & 400 children
Action. Edith + 1yr old baby are evacuees. Husband is amongst the crowd of men waving goodbye.
Plot. Edith and Roy cling to believe they will meet again but "lost in the rain or snow"
Selection for scene. This is a love story not a war book. but without the fall of Singapore and their enforced separation there would be no story.
Other ideas will be considered.
Note SS Countess of Ashvale - pictures are on internet.
Back cover words
In 1941 when the Japanese attacked Singapore the Tulleys, Roy, Edith, and son Albert have to face their own separate destiny, Roy as a PoW, Edith to sail away with her baby into the unknown. No one entirely escapes the privations of war, today, tomorrow, or in years to come. Can Roy and Edith's love bring them together again, and if so where, and if so when?

```html
<!DOCTYPE html>
<html lang="en">
<head>
<meta charset="utf-8">
<title>Lost in the Rain, Lost in the Snow — Trevor Hanley</title>
<link rel="stylesheet" href="https://fonts.googleapis.com/css2?family=Abril+Fatface&family=Archivo:wght@800&display=swap">
<style>
  :root {
    --page: #ffffff;
    --band-orange: #f24a10;
    --author-yellow: #f2ef1e;
    --author-outline: #3b2a10;
    --title-blue: #1f3fe0;
    --title-red: #ea1b0c;
    --title-outline: #f7f21e;
  }
  * { margin: 0; padding: 0; box-sizing: border-box; }
  html, body {
    width: 1200px;
    height: 1200px;
    overflow: hidden;
    background: var(--page);
  }
  .canvas {
    position: relative;
    width: 1200px;
    height: 1200px;
    overflow: hidden;
  }
  .cover {
    position: absolute;
    left: 138px;
    top: 0;
    width: 918px;
    height: 1200px;
    overflow: hidden;
  }
  .cover-art {
    position: absolute;
    inset: 0;
    width: 918px;
    height: 1200px;
  }
  .author {
    position: absolute;
    top: 12px;
    left: 0;
    width: 918px;
    text-align: center;
    font-family: "Archivo", "Arial Black", sans-serif;
    font-weight: 800;
    font-size: 70px;
    letter-spacing: 15px;
    line-height: 1;
    color: var(--author-yellow);
    -webkit-text-stroke: 3px var(--author-outline);
    paint-order: stroke fill;
  }
  .title {
    position: absolute;
    inset: 0;
    font-family: "Abril Fatface", "Bodoni Moda", serif;
    font-weight: 400;
  }
  .title-line {
    position: absolute;
    line-height: 1;
    white-space: nowrap;
    paint-order: stroke fill;
  }
  .title-lead {
    color: var(--title-blue);
    -webkit-text-stroke: 4px #ffffff;
  }
  .title-key {
    color: var(--title-red);
    -webkit-text-stroke: 10px var(--title-outline);
    font-size: 190px;
  }
  .lead-first  { left: 12px;  top: 156px; font-size: 96px;  letter-spacing: 10px; }
  .key-first   { left: 78px;  top: 319px; letter-spacing: 46px; }
  .lead-second { left: 162px; top: 616px; font-size: 104px; letter-spacing: 6px; }
  .key-second  { left: 366px; top: 829px; letter-spacing: 15px; }
</style>
</head>
<body>
<main class="canvas">
  <section class="cover">
    <svg class="cover-art" viewBox="0 0 918 1200" xmlns="http://www.w3.org/2000/svg">
      <defs>
        <radialGradient id="skyGradient" cx="50%" cy="45%" r="70%">
          <stop offset="0%" stop-color="#cfe2f5"/>
          <stop offset="100%" stop-color="#a9c9ea"/>
        </radialGradient>
        <radialGradient id="ornamentGradient" cx="50%" cy="50%" r="50%">
          <stop offset="0%" stop-color="#e3d3ab"/>
          <stop offset="65%" stop-color="#cdb789" stop-opacity="0.8"/>
          <stop offset="100%" stop-color="#b79f6e" stop-opacity="0"/>
        </radialGradient>
        <linearGradient id="figureGradient" x1="0" y1="0" x2="0" y2="1">
          <stop offset="0%" stop-color="#1c1c1c"/>
          <stop offset="100%" stop-color="#050505"/>
        </linearGradient>
        <linearGradient id="harbourGradient" x1="0" y1="0" x2="0" y2="1">
          <stop offset="0%" stop-color="#4a4a4a"/>
          <stop offset="60%" stop-color="#8a8a8a"/>
          <stop offset="100%" stop-color="#d6d6d6"/>
        </linearGradient>
        <filter id="softEdge" x="-30%" y="-30%" width="160%" height="160%">
          <feGaussianBlur stdDeviation="14"/>
        </filter>
        <filter id="softHarbour" x="-10%" y="-40%" width="120%" height="180%">
          <feGaussianBlur stdDeviation="10"/>
        </filter>
      </defs>

      <rect class="sky-texture" width="918" height="1200" fill="url(#skyGradient)"
            role="img" aria-label="Brushed pale blue textured backdrop"/>

      <ellipse class="ornament-swirl" cx="470" cy="430" rx="500" ry="400" fill="url(#ornamentGradient)"
               role="img" aria-label="Gilded swirling filigree ornament behind the title"/>

      <path class="author-band" d="M0 0 H918 V98 Q459 132 0 122 Z" fill="var(--band-orange)"/>

      <ellipse class="husband-silhouette" cx="800" cy="590" rx="86" ry="290"
               fill="url(#figureGradient)" filter="url(#softEdge)" opacity="0.92"
               role="img" aria-label="Silhouette of a man in a long coat standing alone, watching"/>

      <ellipse class="mother-child-silhouette" cx="160" cy="980" rx="122" ry="270"
               fill="url(#figureGradient)" filter="url(#softEdge)" opacity="0.92"
               role="img" aria-label="Silhouette of a mother holding her young child"/>

      <ellipse class="harbour-skyline" cx="468" cy="1175" rx="400" ry="90"
               fill="url(#harbourGradient)" filter="url(#softHarbour)"
               role="img" aria-label="Grey outline of the evacuation ship at the docks"/>
    </svg>

    <p class="author">Trevor Hanley</p>

    <h1 class="title">
      <span class="title-line title-lead lead-first">Lost in the</span>
      <span class="title-line title-key key-first">Rain</span>
      <span class="title-line title-lead lead-second">Lost in the</span>
      <span class="title-line title-key key-second">Snow</span>
    </h1>
  </section>
</main>
</body>
</html>
```